ちょっと急いでおりまして、
当方デザインをする時間がないので、
アウトソーシングしたいと思います。

文章、と構成だけを作りましたので、
宜しければ、お願い致します。

TAVELIA JAPAN で使用する、
お客さまにブランディングするための、
青嶺かやどり の パンフレットです。

PDFで、説明文を記載致しますので、
また見ておいて下さい。

画像素材も、添付させて頂きます。
「青嶺かやどり・かやたまご」を使うフォントは、
明朝体です。アウトラインしたデータも
添付いたします。それを活用下さい。

A4サイズ (裏・表)
両面カラーでで作っていただけると幸いです。

※もしかすると、A0サイズで引き伸ばしてつかうかもしれません。
どうぞよろしくお願い致します。

何か御不明な点がございましたら、お気軽に
ご質問ください。

当社青嶺かやどりの商品ページです。
参考にして下さい。
http://item.shopmarket-example.jp/poultry-hoshino/20004681/

青嶺かやどり協議会の ページです。
http://www.kayadori-example.com/
素材を添付いたします。レイヤーを使っておりますので、分解してください。
このページにある

の画像のような感じで、要約していただけると
幸いです。
画像を追加いたしました。
タイトルが、4Aに なってました。

すみません。A4ポスターです。
循環型の 111 のような 感じで、

ぐるっと 回る ように わかりやすく つくって頂けると幸いです。
かやどりの アニメーションデータは、

aiファイル イラストレーターの
かやたまご に 入っています。

レイヤーで組んでいますが、それを修正して作って下さい。
素材 画像を追加いたしました。
素材追加いたします。

111、222、333、444画像は、見本画像です。
イメージの参考になるかも?と思いまして、
かやどり からでる 副産物の 鶏糞堆肥もっこもこ の画像を 追加いたします。

裏側の、一番重要な情報を綺麗にまとめてくださりました。
そして、私達が やっていることに対して 共感頂けたことが大きかったです。
少し修正頂きたい部分がありますので、御連絡頂けると幸いです。

皆様 急な対応、ありがとうございます。
10件も御応募いただけるとは思っても居なかったのと、
そして、みなさんからの提案が本当に良かったので。
こちらとしても 悩ましかったです。
御提案くださった皆様。本当に、ありがとうございましたm(__)m

```html
<!DOCTYPE html>
<html lang="ja">
<head>
<meta charset="utf-8">
<title>青嶺かやどり・かやたまごとは?</title>
<link rel="stylesheet" href="https://fonts.googleapis.com/css2?family=Shippori+Mincho:wght@600;800&family=Noto+Sans+JP:wght@400;700&display=swap">
<style>
:root{
  --pink:#e04f73;
  --pink-soft:#f7c6d2;
  --pink-pale:#fdeef2;
  --ink:#4a3a36;
  --gold:#f2b23c;
  --cream:#fbf3e4;
  --white:#ffffff;
}
*{margin:0;padding:0;box-sizing:border-box}
html,body{width:846px;height:1200px;overflow:hidden;background:var(--white)}
.poster{position:relative;width:846px;height:1200px;font-family:"Noto Sans JP",sans-serif;color:var(--ink)}
.abs{position:absolute}
.mincho{font-family:"Shippori Mincho",serif}
.main-title{left:40px;top:18px;font-size:42px;font-weight:800;color:var(--pink);letter-spacing:2px}
.title-rule{left:40px;top:80px;width:766px;height:3px;background:var(--pink-soft)}
.section-head{font-family:"Shippori Mincho",serif;font-weight:800;color:var(--pink);font-size:30px}
.section-head::after{content:"";display:block;width:100%;height:4px;margin-top:4px;background:linear-gradient(90deg,var(--pink),var(--pink-soft))}
.lead-tag{left:40px;top:150px;width:370px;padding:6px 10px;background:var(--pink-pale);color:var(--pink);font-weight:700;font-size:15px;border-left:5px solid var(--pink)}
.body-text{font-size:12.5px;line-height:1.75}
.photo{border-radius:6px}
.note-box{left:440px;top:125px;width:170px;height:170px;background:var(--cream);padding:12px;border-radius:6px 0 0 6px}
.note-box h3{font-family:"Shippori Mincho",serif;color:var(--pink);font-size:15px;line-height:1.4;margin-bottom:6px}
.note-box p{font-size:11px;line-height:1.65}
.cycle-title-small{left:40px;top:680px;font-size:34px;font-weight:800;color:var(--pink)}
.cycle-title-big{left:36px;top:730px;font-size:76px;font-weight:800;color:var(--pink);letter-spacing:4px}
.compost{left:40px;top:930px;width:260px;height:240px;background:var(--gold);border-radius:10px;padding:16px;color:var(--white)}
.compost .kicker{font-size:13px;font-weight:700}
.compost h3{font-family:"Shippori Mincho",serif;font-size:30px;line-height:1.2;margin:2px 0 10px}
.compost p{font-size:11.5px;line-height:1.7}
.step{position:absolute;width:104px;height:104px;margin:-52px 0 0 -52px;border-radius:50%;background:var(--white);border:3px solid var(--pink);display:flex;flex-direction:column;align-items:center;justify-content:center;text-align:center;padding:8px}
.step .num{font-family:"Shippori Mincho",serif;font-weight:800;color:var(--pink);font-size:24px;line-height:1}
.step .txt{font-size:11px;line-height:1.35;margin-top:3px}
</style>
</head>
<body>
<div class="poster">
  <h1 class="abs main-title mincho">青嶺かやどり・かやたまごとは?</h1>
  <div class="abs title-rule"></div>

  <h2 class="abs section-head" style="left:40px;top:96px;width:370px">美味しさの秘密</h2>
  <div class="abs lead-tag">青嶺の梅酢を飼料にした贅沢な鶏</div>
  <p class="abs body-text" style="left:40px;top:192px;width:370px">
    青嶺山の麓に広がる梅の里で、梅干作りの際に生まれる梅酢を飼料に混ぜて育てています。梅酢に含まれるクエン酸やポリフェノールが鶏の健康を支え、臭みが少なく、旨みとコクのあるお肉と卵に仕上がります。手間を惜しまず、一羽一羽を大切に育てました。
  </p>

  <div class="abs note-box">
    <h3>自然が豊かな環境ですくすく育てました</h3>
    <p>澄んだ空気と水に恵まれた鶏舎で、ゆったりと育てています。生産者の想いが詰まった自慢の鶏です。</p>
  </div>
  <div class="abs photo" role="img" aria-label="鶏を抱く生産者の写真" style="left:610px;top:125px;width:196px;height:170px;border-radius:0 6px 6px 0;background:linear-gradient(160deg,#c9b9a3,#8c7a66)"></div>

  <div class="abs photo" role="img" aria-label="梅酢を混ぜた飼料の写真" style="left:40px;top:320px;width:370px;height:130px;background:linear-gradient(135deg,#d8a95c,#9c6a2c)"></div>
  <div class="abs photo" role="img" aria-label="緑に囲まれた鶏舎の写真" style="left:440px;top:310px;width:366px;height:140px;background:linear-gradient(180deg,#a9c6de,#7fa06a)"></div>

  <h2 class="abs section-head" style="left:40px;top:470px;width:766px">“かやどり”がはじまった経緯</h2>
  <div class="abs photo" role="img" aria-label="満開の梅の花の写真" style="left:40px;top:525px;width:340px;height:130px;background:linear-gradient(135deg,#f5d3dc,#c98a9a)"></div>
  <p class="abs body-text" style="left:395px;top:525px;width:411px">
    梅干作りの過程で大量に出る梅酢は、長年その使い道が課題でした。地域の養鶏農家と梅農家が手を取り合い、梅酢を鶏の飼料に活かす研究を重ねて誕生したのが「青嶺かやどり」です。青嶺かやどり協議会を中心に、地域の資源を無駄なく循環させる取り組みを続けています。
  </p>

  <div class="abs cycle-title-small mincho">地球にやさしい</div>
  <div class="abs cycle-title-big mincho">循環型</div>

  <svg class="abs" style="left:0;top:0" width="846" height="1200" aria-hidden="true">
    <circle cx="540" cy="945" r="200" fill="none" stroke="var(--pink-soft)" stroke-width="6" stroke-dasharray="14 10"/>
  </svg>
  <div class="abs" role="img" aria-label="かやどりのキャラクターイラスト" style="left:440px;top:845px;width:200px;height:200px;border-radius:50%;background:radial-gradient(circle,#ffffff,#fbe3ea)"></div>

  <div class="step" style="left:540px;top:745px"><span class="num">1</span><span class="txt">梅干作りで<br>梅酢が出る</span></div>
  <div class="step" style="left:669px;top:792px"><span class="num">2</span><span class="txt">梅酢を<br>飼料に配合</span></div>
  <div class="step" style="left:737px;top:910px"><span class="num">3</span><span class="txt">かやどりを<br>元気に育てる</span></div>
  <div class="step" style="left:713px;top:1045px"><span class="num">4</span><span class="txt">お肉と卵を<br>お届け</span></div>
  <div class="step" style="left:608px;top:1133px"><span class="num">5</span><span class="txt">鶏糞を<br>集める</span></div>
  <div class="step" style="left:472px;top:1133px"><span class="num">6</span><span class="txt">堆肥<br>もっこもこに</span></div>
  <div class="step" style="left:367px;top:1045px"><span class="num">7</span><span class="txt">堆肥を<br>梅畑へ</span></div>
  <div class="step" style="left:343px;top:910px"><span class="num">8</span><span class="txt">梅の木が<br>よく育つ</span></div>
  <div class="step" style="left:411px;top:792px"><span class="num">9</span><span class="txt">梅が<br>実る</span></div>

  <div class="abs compost">
    <div class="kicker">鶏糞堆肥</div>
    <h3>“もっこもこ”</h3>
    <p>かやどりの鶏糞を発酵させた、ふんわり柔らかな堆肥です。梅畑の土を豊かにし、また次の梅を育てます。地域の中で資源がめぐる、人にも地球にもやさしい仕組みです。</p>
  </div>
</div>
</body>
</html>
```